Falzflyer-Design für Softwareprodukte
Zielgruppe
Wir bieten mit unserer Produktlinie Morvane Softwareprodukte für Fluggesellschaften und touristische Unternehmen. Unsere Softwarelösungen sind ein Vertriebssystem für Airlines (Inventory), Prozess-basierte Automatisierungen, Buchungsschnittstellen und Datenanalysen. Weiterhin bieten wir diesen Unternehmen Custom Development und Beratungsdienstleistungen an.
Aufgabenstellung
Wir benötigen einen Falzflyer. Die Maße sind in einem Datenblatt von unserer Druckerei enthalten.
Weiterhin haben wir unser Logo und unserem Color Code hochgeladen. In einem pdf haben wir zusätzlich die Inhalte zusammengefasst (aussen und innen), die im Flyer aufgeführt werden sollen (noch nicht alles ist auf unserer Website verfügbar).
Einige Bilder, die wir auf der Website nutzen bzw. nutzen werden, findet ihr dort auch . Es kann aber gerne anderes Bildmaterial verwendet werden.
Wir überarbeiten gerade unsere Website und nutzen neben den unterschiedlichen Grautönen vorrangig #4b75e5, #00bac9 und folgende Schriftarten: Pragrati Narrow für Überschriften, Open Sans für Texte
Flyer wird ausschließlich in Englisch benötigt.

```html
<!DOCTYPE html>
<html lang="en">
<head>
<meta charset="utf-8">
<title>Aerolance Trifold Flyer – Colour Versions</title>
<link href="https://fonts.googleapis.com/css2?family=Open+Sans:wght@300;400;600;700;800&family=Pragati+Narrow:wght@400;700&display=swap" rel="stylesheet">
<style>
:root{
  --bg:#ececec;
  --label:#6f86c9;
  --blue:#4b75e5;
  --lavender:#7f93cc;
  --lavender-dark:#6c80bd;
  --ink-blue:#5b6fb3;
  --teal:#1fb1be;
  --teal-bright:#13b8cc;
  --teal-accent:#00bac9;
  --grey-text:#6b6f78;
  --grey-light:#f2f3f6;
  --white:#ffffff;
}
*{box-sizing:border-box;margin:0;padding:0}
html,body{width:1200px;height:4408px;overflow:hidden;background:var(--bg)}
body{font-family:"Open Sans",Arial,sans-serif;color:var(--grey-text);position:relative}
.stage{position:absolute;left:0;width:1200px;height:735px}
.stage:nth-child(even){background:#f1f1f1}
.version-label{position:absolute;left:52px;top:52px;font-family:"Open Sans",Arial,sans-serif;font-weight:300;font-size:34px;letter-spacing:1px;color:var(--label)}
.spread{position:absolute;left:120px;width:960px;height:520px;display:flex;box-shadow:0 24px 40px rgba(0,0,0,.18);background:var(--white)}
.stage.labelled .spread{top:140px}
.stage.plain .spread{top:108px}
.panel{position:relative;width:320px;height:520px;overflow:hidden}
.panel + .panel{border-left:1px solid rgba(0,0,0,.06)}
.photo{position:absolute;left:0;right:0}
.url{position:absolute;left:0;right:0;bottom:16px;text-align:center;font-weight:700;font-size:13px;letter-spacing:.3px;color:var(--ink-blue)}

/* Benefits panel */
.benefits{color:var(--white);padding:34px 26px 0}
.v1 .benefits{background:linear-gradient(180deg,var(--teal) 0%,#29b6c1 70%,#8fd3da 100%)}
.v2 .benefits{background:linear-gradient(180deg,#8a9bd0 0%,#8ea0d2 65%,#c9d2ea 100%)}
.v3 .benefits{background:linear-gradient(180deg,var(--teal-bright) 0%,#1fbccd 65%,#9edde6 100%)}
.benefits h2{font-weight:800;font-size:22px;text-align:center;padding-bottom:10px;border-bottom:1px solid rgba(255,255,255,.55)}
.benefit-list{list-style:none;text-align:center}
.benefit-list li{font-weight:700;font-size:12.5px;line-height:1.2;padding:9px 10px;border-bottom:1px solid rgba(255,255,255,.45)}
.benefit-list li:last-child{border-bottom:none;font-size:14px}
.benefits .photo{bottom:0;height:120px;background:linear-gradient(180deg,rgba(255,255,255,0),rgba(255,255,255,.45))}
.benefits .url{color:var(--white);bottom:14px}

/* Contact panel */
.contact{background:var(--lavender)}
.contact .photo.city{top:0;height:150px;background:linear-gradient(180deg,#b9c9de 0%,#8ea3bd 55%,#6f7f93 100%)}
.badge{position:absolute;left:50%;transform:translateX(-50%);width:54px;height:54px;border-radius:50%;background:var(--white);display:flex;align-items:center;justify-content:center}
.contact .badge{top:122px}
.contact h2{position:absolute;top:188px;left:0;right:0;text-align:center;color:var(--white);font-weight:800;font-size:21px;line-height:1.05}
.contact-list{position:absolute;top:258px;left:0;right:0;list-style:none;text-align:center;color:var(--white);font-weight:600;font-size:9.5px}
.contact-list li{margin-bottom:12px}
.ring{display:block;margin:0 auto 5px;width:20px;height:20px}
.contact .url{color:var(--white)}

/* Cover panel */
.cover{background:linear-gradient(180deg,#f7f8fb 0%,#eef0f5 100%)}
.wordmark{position:absolute;top:22px;right:26px;display:flex;align-items:center;gap:8px;font-weight:400;font-size:28px;color:#8d9098}
.wordmark-dot{width:12px;height:12px;border-radius:50%;background:var(--teal-accent)}
.cover .photo.jet{top:64px;height:170px;background:linear-gradient(160deg,#dfe4ec 0%,#c3cad6 50%,#eef0f4 100%)}
.tagline{position:absolute;left:0;right:0;text-align:center;line-height:1.05}
.tagline .small{display:block;font-weight:700;font-size:15px;color:#7a7e87}
.tagline .strong{display:block;font-weight:800;font-size:22px;color:var(--ink-blue)}
.tagline.goal{top:262px}
.tagline.job{top:348px}
.cover-band{position:absolute;left:0;right:0;bottom:0;height:46px;background:var(--lavender-dark)}
.cover .url{color:var(--white);bottom:15px}

/* Inside panels */
.inside{background:linear-gradient(180deg,#eef1f7 0%,#f6f7fa 55%,#e9edf4 100%);padding:0 22px}
.inside .photo.head{top:0;height:120px;background:linear-gradient(180deg,#c9d3e3 0%,#dfe5ee 100%)}
.inside .badge{top:96px;width:48px;height:48px;background:var(--teal-accent)}
.inside h3{position:absolute;top:154px;left:18px;right:18px;text-align:center;font-weight:800;font-size:17px;line-height:1.05;color:var(--ink-blue)}
.intro{position:absolute;top:198px;left:24px;right:24px;font-size:8px;line-height:1.35;text-align:center;color:#7a7e87}
.features{position:absolute;top:236px;left:24px;right:20px}
.features h4{font-weight:800;font-size:9px;color:#555;margin-bottom:6px}
.feature-group{margin-bottom:8px}
.feature-group strong{display:block;font-size:10px;color:var(--ink-blue);margin-bottom:2px}
.feature-group ul,.feature-simple{list-style:none;font-size:8px;line-height:1.45;color:#777}
.feature-group li::before,.feature-simple li::before{content:"○ ";color:var(--teal-accent)}
.custom-copy{position:absolute;top:204px;left:24px;right:24px;font-size:8.5px;line-height:1.4;text-align:center;color:#7a7e87}
.custom-copy p{margin-bottom:8px}
.inside .photo.jet-large{bottom:0;height:200px;background:linear-gradient(180deg,rgba(230,234,242,0) 0%,#d5dbe6 45%,#e7eaf0 100%)}
</style>
</head>
<body>

<!-- ===== Version 1 outside ===== -->
<section class="stage labelled v1" style="top:0">
  <div class="version-label">FARBVERSION 1</div>
  <div class="spread">
    <div class="panel benefits">
      <h2>Benefits</h2>
      <ul class="benefit-list">
        <li>Maximize your<br>revenue</li>
        <li>Reduce your<br>distribution cost</li>
        <li>Use your competitive<br>advantage</li>
        <li>Focus on business<br>processes</li>
        <li>Customize Morvane<br>quick and easy</li>
        <li>Eliminate<br>complexity</li>
        <li>Pay-as-you-go with no<br>huge up-front<br>costs (SaaS &amp; PaaS)</li>
      </ul>
      <div class="photo" role="img" aria-label="Faint photo of an airliner in flight"></div>
    </div>
    <div class="panel contact">
      <div class="photo city" role="img" aria-label="Photo of a city skyline with a TV tower"></div>
      <div class="badge"><svg width="28" height="28" viewBox="0 0 28 28"><path d="M4 6h14a3 3 0 0 1 3 3v6a3 3 0 0 1-3 3H10l-5 4v-4a3 3 0 0 1-1-2V9a3 3 0 0 1 0-3z" fill="none" stroke="#00bac9" stroke-width="2"/></svg></div>
      <h2>Get in touch<br>with us</h2>
      <ul class="contact-list">
        <li><svg class="ring" viewBox="0 0 20 20"><circle cx="10" cy="10" r="9" fill="none" stroke="#fff"/><circle cx="10" cy="8" r="3" fill="none" stroke="#fff"/><path d="M5 15c1-3 9-3 10 0" fill="none" stroke="#fff"/></svg>Aerolance GmbH</li>
        <li><svg class="ring" viewBox="0 0 20 20"><circle cx="10" cy="10" r="9" fill="none" stroke="#fff"/><path d="M10 15s-4-4-4-7a4 4 0 0 1 8 0c0 3-4 7-4 7z" fill="none" stroke="#fff"/></svg>Lindenweg 14 | 10115 Berlin</li>
        <li><svg class="ring" viewBox="0 0 20 20"><circle cx="10" cy="10" r="9" fill="none" stroke="#fff"/><path d="M7 5l2 3-1 1c1 2 2 3 3 3l1-1 3 2-1 2c-4 0-8-4-8-8z" fill="none" stroke="#fff"/></svg>Phone: +49 170 55 01 234</li>
        <li><svg class="ring" viewBox="0 0 20 20"><circle cx="10" cy="10" r="9" fill="none" stroke="#fff"/><rect x="5" y="7" width="10" height="7" fill="none" stroke="#fff"/><path d="M5 7l5 4 5-4" fill="none" stroke="#fff"/></svg>info@aerolance.example</li>
      </ul>
      <div class="url">www.aerolance.example</div>
    </div>
    <div class="panel cover">
      <div class="wordmark"><span class="wordmark-dot"></span>Aerolance</div>
      <div class="photo jet" role="img" aria-label="Photo of a jet airliner banking through clouds"></div>
      <div class="tagline goal"><span class="small">UNIFYING TOURISTIC<br>AND AIRLINE BUSINESS</span><span class="strong">IS OUR GOAL</span></div>
      <div class="tagline job"><span class="small">BREAKING THE<br>TECHNOLOGY GAP</span><span class="strong">IS OUR JOB</span></div>
      <div class="cover-band"></div>
      <div class="url">www.aerolance.example</div>
    </div>
  </div>
</section>

<!-- ===== Version 1 inside ===== -->
<section class="stage plain" style="top:735px">
  <div class="spread">
    <div class="panel inside">
      <div class="photo head" role="img" aria-label="Photo of an airliner on the runway"></div>
      <div class="badge"><svg width="24" height="24" viewBox="0 0 24 24"><rect x="6" y="4" width="12" height="16" fill="none" stroke="#fff" stroke-width="2"/><path d="M9 9h6M9 13h6" stroke="#fff" stroke-width="2"/></svg></div>
      <h3>AEROLANCE MORVANE<br>INVENTORY</h3>
      <p class="intro">Full-featured inventory and allotment system for airlines, built to control seats and fares directly.</p>
      <div class="features">
        <h4>KEY FEATURES:</h4>
        <div class="feature-group"><strong>Revenue and Allotment Management</strong><ul><li>Fixed &amp; flexible allotments</li><li>Group &amp; charter control</li></ul></div>
        <div class="feature-group"><strong>Seat Only and Ancillary Management</strong><ul><li>Seat maps &amp; ancillary pricing</li><li>Seat-only sales channels</li></ul></div>
        <div class="feature-group"><strong>Data Processing and API Management</strong><ul><li>Passenger name list processing (PNL/ADL)</li><li>PSS integration (open APIs)</li><li>Post flight processing</li></ul></div>
      </div>
      <div class="url">www.aerolance.example</div>
    </div>
    <div class="panel inside">
      <div class="photo head" role="img" aria-label="Photo of a person working at a laptop"></div>
      <div class="badge"><svg width="24" height="24" viewBox="0 0 24 24"><circle cx="12" cy="12" r="4" fill="none" stroke="#fff" stroke-width="2"/><circle cx="12" cy="12" r="8" fill="none" stroke="#fff" stroke-width="2" stroke-dasharray="3 2"/></svg></div>
      <h3>AEROLANCE MORVANE<br>AUTOMATE</h3>
      <p class="intro">Automate back-office processes and connect systems together for reduced cost and effort.</p>
      <div class="features">
        <h4>KEY FEATURES:</h4>
        <ul class="feature-simple">
          <li>Rule engine - based Revenue integrity</li>
          <li>Back office automation with Queue Management</li>
          <li>Mass rebooking &amp; Reallocation</li>
          <li>Customized communication &amp; invoicing</li>
          <li>Loyalty Program &amp; Branded Fare Management</li>
          <li>Sales channel synchronization</li>
        </ul>
      </div>
      <div class="url">www.aerolance.example</div>
    </div>
    <div class="panel inside">
      <div class="photo head" role="img" aria-label="Photo of an aircraft wing above the clouds"></div>
      <div class="badge"><svg width="24" height="24" viewBox="0 0 24 24"><path d="M5 19V13M10 19V9M15 19V11M20 19V6" stroke="#fff" stroke-width="2.5"/></svg></div>
      <h3>AEROLANCE CUSTOM<br>DEVELOPMENT</h3>
      <div class="custom-copy">
        <p>We provide custom developments using modern agile technologies combined with our extensive airline and touristic knowledge.</p>
        <p>As experienced airline IT developers, we work with you to fully understand your requirements, and commit to deliver within agreed timeframes, to your complete satisfaction.</p>
      </div>
      <div class="photo jet-large" role="img" aria-label="Photo of a jet airliner climbing through clouds"></div>
      <div class="url">www.aerolance.example</div>
    </div>
  </div>
</section>

<!-- ===== Version 2 outside ===== -->
<section class="stage labelled v2" style="top:1470px">
  <div class="version-label">FARBVERSION 2</div>
  <div class="spread">
    <div class="panel benefits">
      <h2>Benefits</h2>
      <ul class="benefit-list">
        <li>Maximize your<br>revenue</li>
        <li>Reduce your<br>distribution cost</li>
        <li>Use your competitive<br>advantage</li>
        <li>Focus on business<br>processes</li>
        <li>Customize Morvane<br>simply and quickly</li>
        <li>Eliminate<br>complexity</li>
        <li>Pay-as-you-go with no<br>huge up-front costs<br>(SaaS &amp; PaaS)</li>
      </ul>
      <div class="photo" role="img" aria-label="Faint photo of an airliner in flight"></div>
      <div class="url">www.aerolance.example</div>
    </div>
    <div class="panel contact">
      <div class="photo city" role="img" aria-label="Photo of a city skyline with a TV tower"></div>
      <div class="badge"><svg width="28" height="28" viewBox="0 0 28 28"><path d="M4 6h14a3 3 0 0 1 3 3v6a3 3 0 0 1-3 3H10l-5 4v-4a3 3 0 0 1-1-2V9a3 3 0 0 1 0-3z" fill="none" stroke="#00bac9" stroke-width="2"/></svg></div>
      <h2>Get in touch<br>with us</h2>
      <ul class="contact-list">
        <li><svg class="ring" viewBox="0 0 20 20"><circle cx="10" cy="10" r="9" fill="none" stroke="#fff"/><circle cx="10" cy="8" r="3" fill="none" stroke="#fff"/><path d="M5 15c1-3 9-3 10 0" fill="none" stroke="#fff"/></svg>Aerolance GmbH</li>
        <li><svg class="ring" viewBox="0 0 20 20"><circle cx="10" cy="10" r="9" fill="none" stroke="#fff"/><path d="M10 15s-4-4-4-7a4 4 0 0 1 8 0c0 3-4 7-4 7z" fill="none" stroke="#fff"/></svg>Lindenweg 14 | 10115 Berlin</li>
        <li><svg class="ring" viewBox="0 0 20 20"><circle cx="10" cy="10" r="9" fill="none" stroke="#fff"/><path d="M7 5l2 3-1 1c1 2 2 3 3 3l1-1 3 2-1 2c-4 0-8-4-8-8z" fill="none" stroke="#fff"/></svg>Phone: +49 170 55 01 234</li>
        <li><svg class="ring" viewBox="0 0 20 20"><circle cx="10" cy="10" r="9" fill="none" stroke="#fff"/><rect x="5" y="7" width="10" height="7" fill="none" stroke="#fff"/><path d="M5 7l5 4 5-4" fill="none" stroke="#fff"/></svg>info@aerolance.example</li>
      </ul>
      <div class="url">www.aerolance.example</div>
    </div>
    <div class="panel cover">
      <div class="wordmark"><span class="wordmark-dot"></span>Aerolance</div>
      <div class="photo jet" role="img" aria-label="Photo of a jet airliner banking through clouds"></div>
      <div class="tagline goal"><span class="small">UNIFYING TOURISTIC<br>AND AIRLINE BUSINESS</span><span class="strong">IS OUR GOAL</span></div>
      <div class="tagline job"><span class="small">BREAKING THE<br>TECHNOLOGY GAP</span><span class="strong">IS OUR JOB</span></div>
      <div class="cover-band"></div>
      <div class="url">www.aerolance.example</div>
    </div>
  </div>
</section>

<!-- ===== Version 2 inside ===== -->
<section class="stage plain" style="top:2205px">
  <div class="spread">
    <div class="panel inside">
      <div class="photo head" role="img" aria-label="Photo of an airliner on the runway"></div>
      <div class="badge"><svg width="24" height="24" viewBox="0 0 24 24"><rect x="6" y="4" width="12" height="16" fill="none" stroke="#fff" stroke-width="2"/><path d="M9 9h6M9 13h6" stroke="#fff" stroke-width="2"/></svg></div>
      <h3>AEROLANCE MORVANE<br>INVENTORY</h3>
      <p class="intro">Full-featured inventory and allotment system for airlines, built to control seats and fares directly.</p>
      <div class="features">
        <h4>KEY FEATURES:</h4>
        <div class="feature-group"><strong>Revenue and Allotment Management</strong><ul><li>Fixed &amp; flexible allotments</li><li>Group &amp; charter control</li></ul></div>
        <div class="feature-group"><strong>Seat Only and Ancillary Management</strong><ul><li>Seat maps &amp; ancillary pricing</li><li>Seat-only sales channels</li></ul></div>
        <div class="feature-group"><strong>Data Processing and API Management</strong><ul><li>Passenger name list processing (PNL/ADL)</li><li>PSS integration (open APIs)</li><li>Post flight processing</li></ul></div>
      </div>
      <div class="url">www.aerolance.example</div>
    </div>
    <div class="panel inside">
      <div class="photo head" role="img" aria-label="Photo of a person working at a laptop"></div>
      <div class="badge"><svg width="24" height="24" viewBox="0 0 24 24"><circle cx="12" cy="12" r="4" fill="none" stroke="#fff" stroke-width="2"/><circle cx="12" cy="12" r="8" fill="none" stroke="#fff" stroke-width="2" stroke-dasharray="3 2"/></svg></div>
      <h3>AEROLANCE MORVANE<br>AUTOMATE</h3>
      <p class="intro">Automate back-office processes and connect systems together for reduced cost and effort.</p>
      <div class="features">
        <h4>KEY FEATURES:</h4>
        <ul class="feature-simple">
          <li>Rule engine - based Revenue integrity</li>
          <li>Back office automation with Queue Management</li>
          <li>Mass rebooking &amp; Reallocation</li>
          <li>Customized communication &amp; invoicing</li>
          <li>Loyalty Program &amp; Branded Fare Management</li>
          <li>Sales channel synchronization</li>
        </ul>
      </div>
      <div class="url">www.aerolance.example</div>
    </div>
    <div class="panel inside">
      <div class="photo head" role="img" aria-label="World map graphic with a small aircraft tail"></div>
      <div class="badge"><svg width="24" height="24" viewBox="0 0 24 24"><path d="M5 19V13M10 19V9M15 19V11M20 19V6" stroke="#fff" stroke-width="2.5"/></svg></div>
      <h3>AEROLANCE CUSTOM<br>DEVELOPMENT</h3>
      <div class="custom-copy">
        <p>We provide custom developments using modern agile technologies combined with our extensive airline and touristic knowledge.</p>
        <p>As experienced airline IT developers, we work with you to fully understand your requirements, and commit to deliver within agreed timeframes, to your complete satisfaction.</p>
      </div>
      <div class="photo jet-large" role="img" aria-label="Photo of a jet airliner climbing through clouds"></div>
      <div class="url">www.aerolance.example</div>
    </div>
  </div>
</section>

<!-- ===== Version 3 outside ===== -->
<section class="stage labelled v3" style="top:2940px">
  <div class="version-label">FARBVERSION 3</div>
  <div class="spread">
    <div class="panel benefits">
      <h2>Benefits</h2>
      <ul class="benefit-list">
        <li>Maximize your<br>revenue</li>
        <li>Reduce your<br>distribution cost</li>
        <li>Use your competitive<br>advantage</li>
        <li>Focus on business<br>processes</li>
        <li>Customize Morvane<br>quick and easy</li>
        <li>Eliminate<br>complexity</li>
        <li>Pay-as-you-go with no<br>huge up-front<br>costs (SaaS &amp; PaaS)</li>
      </ul>
      <div class="photo" role="img" aria-label="Faint photo of an airliner in flight"></div>
      <div class="url">www.aerolance.example</div>
    </div>
    <div class="panel contact">
      <div class="photo city" role="img" aria-label="Photo of a city skyline with a TV tower"></div>
      <div class="badge"><svg width="28" height="28" viewBox="0 0 28 28"><path d="M4 6h14a3 3 0 0 1 3 3v6a3 3 0 0 1-3 3H10l-5 4v-4a3 3 0 0 1-1-2V9a3 3 0 0 1 0-3z" fill="none" stroke="#00bac9" stroke-width="2"/></svg></div>
      <h2>Get in touch<br>with us</h2>
      <ul class="contact-list">
        <li><svg class="ring" viewBox="0 0 20 20"><circle cx="10" cy="10" r="10" fill="#00bac9"/><circle cx="10" cy="8" r="3" fill="#fff"/><path d="M5 15c1-3 9-3 10 0" fill="#fff"/></svg>Aerolance GmbH</li>
        <li><svg class="ring" viewBox="0 0 20 20"><circle cx="10" cy="10" r="10" fill="#00bac9"/><path d="M10 15s-4-4-4-7a4 4 0 0 1 8 0c0 3-4 7-4 7z" fill="#fff"/></svg>Lindenweg 14 | 10115 Berlin</li>
        <li><svg class="ring" viewBox="0 0 20 20"><circle cx="10" cy="10" r="10" fill="#00bac9"/><path d="M7 5l2 3-1 1c1 2 2 3 3 3l1-1 3 2-1 2c-4 0-8-4-8-8z" fill="#fff"/></svg>Phone: +49 170 55 01 234</li>
        <li><svg class="ring" viewBox="0 0 20 20"><circle cx="10" cy="10" r="10" fill="#00bac9"/><rect x="5" y="7" width="10" height="7" fill="#fff"/><path d="M5 7l5 4 5-4" fill="none" stroke="#00bac9"/></svg>info@aerolance.example</li>
      </ul>
      <div class="url">www.aerolance.example</div>
    </div>
    <div class="panel cover">
      <div class="wordmark"><span class="wordmark-dot"></span>Aerolance</div>
      <div class="photo jet" role="img" aria-label="Photo of a jet airliner banking through clouds"></div>
      <div class="tagline goal"><span class="small">UNIFYING TOURISTIC<br>AND AIRLINE BUSINESS</span><span class="strong">IS OUR GOAL</span></div>
      <div class="tagline job"><span class="small">BREAKING THE<br>TECHNOLOGY GAP</span><span class="strong">IS OUR JOB</span></div>
      <div class="cover-band"></div>
      <div class="url">www.aerolance.example</div>
    </div>
  </div>
</section>

<!-- ===== Version 3 inside ===== -->
<section class="stage plain" style="top:3675px;height:733px">
  <div class="spread">
    <div class="panel inside">
      <div class="photo head" role="img" aria-label="Photo of an airliner on the runway"></div>
      <div class="badge"><svg width="24" height="24" viewBox="0 0 24 24"><rect x="6" y="4" width="12" height="16" fill="none" stroke="#fff" stroke-width="2"/><path d="M9 9h6M9 13h6" stroke="#fff" stroke-width="2"/></svg></div>
      <h3>AEROLANCE MORVANE<br>INVENTORY</h3>
      <p class="intro">Full-featured inventory and allotment system for airlines, built to control seats and fares directly.</p>
      <div class="features">
        <h4>KEY FEATURES:</h4>
        <div class="feature-group"><strong>Revenue and Allotment Management</strong><ul><li>Fixed &amp; flexible allotments</li><li>Group &amp; charter control</li></ul></div>
        <div class="feature-group"><strong>Seat Only and Ancillary Management</strong><ul><li>Seat maps &amp; ancillary pricing</li><li>Seat-only sales channels</li></ul></div>
        <div class="feature-group"><strong>Data Processing and API Management</strong><ul><li>Passenger name list processing (PNL/ADL)</li><li>PSS integration (open APIs)</li><li>Post flight processing</li></ul></div>
      </div>
      <div class="url">www.aerolance.example</div>
    </div>
    <div class="panel inside">
      <div class="photo head" role="img" aria-label="Photo of a person working at a laptop"></div>
      <div class="badge"><svg width="24" height="24" viewBox="0 0 24 24"><circle cx="12" cy="12" r="4" fill="none" stroke="#fff" stroke-width="2"/><circle cx="12" cy="12" r="8" fill="none" stroke="#fff" stroke-width="2" stroke-dasharray="3 2"/></svg></div>
      <h3>AEROLANCE MORVANE<br>AUTOMATE</h3>
      <p class="intro">Automate back-office processes and connect systems together for reduced cost and effort.</p>
      <div class="features">
        <h4>KEY FEATURES:</h4>
        <ul class="feature-simple">
          <li>Rule engine - based Revenue integrity</li>
          <li>Back office automation with Queue Management</li>
          <li>Mass rebooking &amp; Reallocation</li>
          <li>Customized communication &amp; invoicing</li>
          <li>Loyalty Program &amp; Branded Fare Management</li>
          <li>Sales channel synchronization</li>
        </ul>
      </div>
      <div class="url">www.aerolance.example</div>
    </div>
    <div class="panel inside">
      <div class="photo head" role="img" aria-label="World map graphic with a small aircraft tail"></div>
      <div class="badge"><svg width="24" height="24" viewBox="0 0 24 24"><path d="M5 19V13M10 19V9M15 19V11M20 19V6" stroke="#fff" stroke-width="2.5"/></svg></div>
      <h3>AEROLANCE CUSTOM<br>DEVELOPMENT</h3>
      <div class="custom-copy">
        <p>We provide custom developments using modern agile technologies combined with our extensive airline and touristic knowledge.</p>
        <p>As experienced airline IT developers, we work with you to fully understand your requirements, and commit to deliver within agreed timeframes, to your complete satisfaction.</p>
      </div>
      <div class="photo jet-large" role="img" aria-label="Photo of a jet airliner climbing through clouds"></div>
      <div class="url">www.aerolance.example</div>
    </div>
  </div>
</section>

</body>
</html>
```